Brightfold Systems, a software development company, needs a website

We need a website to promote our software development company. The company is brand new and we want to market ourselves. We develop all kinds of software from web applications, to desktop applications, to mobile applications. Small company, not a lot of history, just need something flashy.

```html
<!DOCTYPE html>
<html lang="en">
<head>
<meta charset="utf-8">
<title>Brightfold Systems Inc.</title>
<link href="https://fonts.googleapis.com/css2?family=Poppins:wght@400;500;600&family=Jost:wght@400;500&display=swap" rel="stylesheet">
<style>
:root{
  --blue:#1b92c9;
  --blue-dark:#157fb0;
  --hero:#5f9dbf;
  --green:#a7c93c;
  --ink:#2f2f2f;
  --text:#444;
  --muted:#666;
  --card:#f3f3f3;
  --line:#d8d8d8;
  --white:#fff;
}
*{box-sizing:border-box;margin:0;padding:0}
html,body{width:1200px;height:2557px;overflow:hidden;background:var(--white)}
body{position:relative;font-family:'Poppins',sans-serif;color:var(--text)}
.abs{position:absolute}
.btn{position:absolute;display:flex;align-items:center;justify-content:center;color:var(--white);font-family:'Jost',sans-serif;font-size:16px;text-decoration:none}
.btn-blue{background:var(--blue)}
.btn-green{background:var(--green)}
.brand{font-family:'Poppins',sans-serif;font-weight:600;color:var(--ink)}
/* header */
.site-header .brand{left:150px;top:38px;font-size:36px;letter-spacing:-.3px}
/* hero */
.hero{left:0;top:95px;width:1200px;height:522px;background:var(--hero)}
.hero-art{left:153px;top:20px;width:444px;height:480px;background:radial-gradient(ellipse at 50% 55%,#e9f1f6 0%,#9cc3d9 45%,rgba(95,157,191,0) 72%)}
.hero-title{right:143px;top:130px;font-family:'Jost',sans-serif;font-size:41px;color:var(--white);font-weight:400}
.hero-sub{right:143px;top:190px;width:460px;text-align:right;font-family:'Jost',sans-serif;font-size:24px;line-height:36px;color:var(--white)}
/* services */
.service{top:672px;width:288px;height:301px;background:var(--card);box-shadow:2px 3px 5px rgba(0,0,0,.28);text-align:center;padding:22px 18px 0}
.service.active{background:var(--blue);color:var(--white)}
.service svg{display:block;margin:0 auto}
.service h3{font-weight:500;font-size:17px;margin-top:14px;color:var(--ink)}
.service.active h3{color:var(--white)}
.service p{font-size:12.5px;line-height:23px;margin-top:8px}
/* steps */
.section-title{width:1200px;text-align:center;font-family:'Jost',sans-serif;font-weight:400;color:var(--ink)}
.step-circle{width:188px;height:188px;border-radius:50%;background:var(--blue);border:3px solid var(--green);display:flex;align-items:center;justify-content:center}
.step-num{width:52px;height:52px;border-radius:50%;background:var(--green);border:3px solid var(--white);color:var(--white);font-family:'Jost',sans-serif;font-size:34px;display:flex;align-items:center;justify-content:center}
.step-label{width:320px;text-align:center;font-weight:500;font-size:17px;color:var(--ink)}
/* map */
.map{left:0;top:1522px;width:1200px;height:290px;background:linear-gradient(135deg,#e6e9ec 0%,#d3dae1 45%,#e4e7ea 70%,#cfd7df 100%)}
.map-card{left:683px;top:1611px;width:215px;height:82px;background:var(--blue);color:var(--white);padding:10px 14px;box-shadow:2px 3px 5px rgba(0,0,0,.25)}
.map-card strong{display:block;font-weight:500;font-size:14px}
.map-card span{font-size:12.5px;line-height:19px}
/* contact */
.label{font-size:14px;color:var(--ink)}
.contact-item{left:141px;display:flex;gap:16px;font-size:13px;line-height:19px;color:var(--muted)}
.contact-item svg{flex:none;margin-top:1px}
.abn{left:141px;top:2015px;font-size:14px;font-weight:600;color:var(--blue)}
.abn span{color:var(--text);font-weight:500}
.social{top:2060px;width:27px;height:27px;border:1.5px solid var(--blue)}
.footer-brand{left:395px;top:1945px;width:300px;text-align:center;font-size:34px;line-height:42px;font-weight:500}
.field{border:1px solid var(--line);font-size:12px;color:var(--ink);padding:8px 8px;background:var(--white)}
/* about */
.about-text{left:165px;width:870px;text-align:center;font-size:12.5px;line-height:24.7px;color:var(--text)}
.site-footer{left:0;top:2519px;width:1200px;height:38px;background:var(--blue);color:var(--white);font-size:12.5px;display:flex;align-items:center;justify-content:center}
</style>
</head>
<body>

<header class="site-header">
  <div class="abs brand">Brightfold Systems Inc.</div>
  <a class="btn btn-blue" style="left:707px;top:43px;width:196px;height:30px;font-size:15px">Get Your Solution Now!</a>
  <a class="btn btn-green" style="left:915px;top:43px;width:143px;height:30px;font-size:16px;gap:10px">
    <svg width="18" height="18" viewBox="0 0 24 24" fill="none" stroke="#fff" stroke-width="2"><path d="M5 3h4l2 5-2.5 1.5a11 11 0 0 0 6 6L16 13l5 2v4a2 2 0 0 1-2 2A16 16 0 0 1 3 5a2 2 0 0 1 2-2z"/></svg>
    123.555.0198
  </a>
</header>

<section class="abs hero">
  <div class="abs hero-art" role="img" aria-label="Illustration of a businessman with a briefcase standing on a rising arrow, reaching toward a chart target"></div>
  <h1 class="abs hero-title">We Develop All Kinds of</h1>
  <p class="abs hero-sub">Software From Web Applications, To Desktop Applications, To Mobile Applications</p>
  <a class="btn btn-green" style="left:820px;top:312px;width:238px;height:38px;font-size:18px">Get Your Solution Now!</a>
</section>

<section class="services">
  <article class="abs service" style="left:141px">
    <svg width="120" height="96" viewBox="0 0 120 96" fill="none" stroke="#1b92c9" stroke-width="4"><rect x="16" y="6" width="88" height="62" rx="4"/><path d="M4 76h112l-6 10H10z"/><path d="M46 26l-12 11 12 11M74 26l12 11-12 11M64 22l-8 30"/></svg>
    <h3>Web Applications</h3>
    <p>Lorem ipsum dolor sit amet, sectetuer adipiscin ga mortis nisl aliquip fdafe ea commodo consequatLorem ipsum dolor sit amet, sectetuer adipiscin ga mortis nisl aliquip fdafe ea.</p>
  </article>
  <article class="abs service active" style="left:457px">
    <svg width="120" height="96" viewBox="0 0 120 96" fill="none" stroke="#fff" stroke-width="4"><rect x="10" y="4" width="100" height="68" rx="4"/><path d="M48 72l-4 14h32l-4-14M36 88h48"/><path d="M46 16h26M46 28h20M52 40h22M46 52h18M56 16v40" stroke-width="5"/></svg>
    <h3>Desktop Applications</h3>
    <p>Lorem ipsum dolor sit amet, sectetuer adipiscin ga mortis nisl aliquip fdafe ea commodo consequatLorem ipsum dolor sit amet, sectetuer adipiscin ga mortis nisl aliquip fdafe ea.</p>
  </article>
  <article class="abs service" style="left:770px">
    <svg width="120" height="96" viewBox="0 0 120 96" fill="none" stroke="#1b92c9" stroke-width="3"><rect x="32" y="2" width="46" height="90" rx="6"/><path d="M48 10h14M50 84h10"/><circle cx="55" cy="47" r="8"/><circle cx="55" cy="47" r="15" stroke-dasharray="6 4"/><path d="M82 38h18M82 47h24M82 56h18"/></svg>
    <h3>Mobile Applications</h3>
    <p>Lorem ipsum dolor sit amet, sectetuer adipiscin ga mortis nisl aliquip fdafe ea commodo consequatLorem ipsum dolor sit amet, sectetuer adipiscin ga mortis nisl aliquip fdafe ea.</p>
  </article>
</section>

<section class="how-it-works">
  <h2 class="abs section-title" style="left:0;top:1096px;font-size:27px">How It Works</h2>

  <div class="abs step-circle" style="left:162px;top:1152px">
    <svg width="120" height="70" viewBox="0 0 120 70" fill="none" stroke="#fff" stroke-width="3.5"><rect x="38" y="8" width="72" height="52"/><path d="M38 8l36 30 36-30"/><path d="M6 26h24M12 36h18M2 46h28"/></svg>
  </div>
  <div class="abs step-num" style="left:158px;top:1150px">1</div>
  <div class="abs step-label" style="left:96px;top:1357px">Send Us Your Specs</div>

  <div class="abs step-circle" style="left:479px;top:1152px">
    <svg width="90" height="100" viewBox="0 0 90 100" fill="none" stroke="#fff" stroke-width="3.5"><rect x="14" y="28" width="12" height="32"/><path d="M26 32l14-20c6 0 8 4 6 14h22c5 0 7 5 4 9 3 3 2 8-2 9 2 4 0 8-4 8H26"/><path d="M15 72l3 7 7 1-5 5 1 7-6-4-6 4 1-7-5-5 7-1zM45 72l3 7 7 1-5 5 1 7-6-4-6 4 1-7-5-5 7-1zM75 72l3 7 7 1-5 5 1 7-6-4-6 4 1-7-5-5 7-1z" stroke-width="2.5"/></svg>
  </div>
  <div class="abs step-num" style="left:475px;top:1150px">2</div>
  <div class="abs step-label" style="left:413px;top:1357px">Review And Choose Options</div>

  <div class="abs step-circle" style="left:792px;top:1152px">
    <svg width="100" height="100" viewBox="0 0 100 100" fill="none" stroke="#fff" stroke-width="3"><circle cx="22" cy="30" r="7"/><path d="M12 88V48h20v40"/><path d="M36 88L62 34l30 54z"/><path d="M62 34V8h22l-4 7 4 7H62"/><path d="M68 16l4 4 7-7"/></svg>
  </div>
  <div class="abs step-num" style="left:788px;top:1150px">3</div>
  <div class="abs step-label" style="left:726px;top:1357px">Complete Successful Project</div>

  <svg class="abs" style="left:378px;top:1232px" width="72" height="28" viewBox="0 0 72 28" fill="#cfcfcf"><circle cx="6" cy="14" r="5"/><circle cx="20" cy="14" r="5"/><circle cx="34" cy="14" r="5"/><path d="M48 2l4-2 16 14-16 14-4-2 13-12z"/></svg>
  <svg class="abs" style="left:696px;top:1232px" width="72" height="28" viewBox="0 0 72 28" fill="#cfcfcf"><circle cx="6" cy="14" r="5"/><circle cx="20" cy="14" r="5"/><circle cx="34" cy="14" r="5"/><path d="M48 2l4-2 16 14-16 14-4-2 13-12z"/></svg>

  <a class="btn btn-green" style="left:426px;top:1418px;width:102px;height:34px;font-size:15px">Get Started</a>
  <a class="btn btn-blue" style="left:534px;top:1418px;width:197px;height:34px;font-size:16px">Get Your Solution Now!</a>
</section>

<section class="location">
  <div class="abs map" role="img" aria-label="Grey road map of the region around the office location"></div>
  <svg class="abs" style="left:640px;top:1630px" width="30" height="38" viewBox="0 0 30 38" fill="none" stroke="#1b92c9" stroke-width="3"><path d="M15 36S3 22 3 14a12 12 0 0 1 24 0c0 8-12 22-12 22z"/><circle cx="15" cy="14" r="4"/></svg>
  <svg class="abs" style="left:669px;top:1632px" width="16" height="22" viewBox="0 0 16 22" fill="#1b92c9"><path d="M16 0v22L0 12z"/></svg>
  <div class="abs map-card"><strong>Brightfold Systems Inc.</strong><span>Street Name, City Name<br>US,&nbsp; NewYork 123458</span></div>
</section>

<section class="contact">
  <div class="abs label" style="left:141px;top:1862px">Contact Us</div>
  <div class="abs contact-item" style="top:1900px">
    <svg width="14" height="18" viewBox="0 0 14 18" fill="none" stroke="#1b92c9" stroke-width="1.6"><path d="M7 17S1 10 1 6.5a6 6 0 0 1 12 0C13 10 7 17 7 17z"/><circle cx="7" cy="6.5" r="2"/></svg>
    <span>Street Name, City Name<br>US,&nbsp; NewYork 123458</span>
  </div>
  <div class="abs contact-item" style="top:1947px">
    <svg width="14" height="16" viewBox="0 0 24 24" fill="none" stroke="#1b92c9" stroke-width="2.2"><path d="M5 3h4l2 5-2.5 1.5a11 11 0 0 0 6 6L16 13l5 2v4a2 2 0 0 1-2 2A16 16 0 0 1 3 5a2 2 0 0 1 2-2z"/></svg>
    <span>123.555.0147</span>
  </div>
  <div class="abs contact-item" style="top:1977px">
    <svg width="14" height="16" viewBox="0 0 14 16" fill="none" stroke="#1b92c9" stroke-width="1.6"><rect x="1" y="3" width="12" height="10"/><path d="M1 3l6 5 6-5"/></svg>
    <span>inquiry@brightfoldsystems.com</span>
  </div>
  <div class="abs abn">ABN: <span style="color:var(--ink)">12 300 4410 7821</span></div>
  <div class="abs social" style="left:141px" aria-label="Social profile"></div>
  <div class="abs social" style="left:175px" aria-label="Social profile"></div>
  <div class="abs social" style="left:209px" aria-label="Social profile"></div>

  <div class="abs brand footer-brand">Brightfold<br>Systems Inc.</div>

  <form class="contact-form">
    <div class="abs label" style="left:725px;top:1862px">Get Your Solution Now!</div>
    <div class="abs field" style="left:724px;top:1904px;width:334px;height:34px">First Name</div>
    <div class="abs field" style="left:724px;top:1941px;width:162px;height:34px">Email</div>
    <div class="abs field" style="left:897px;top:1941px;width:161px;height:34px">Phone</div>
    <div class="abs field" style="left:724px;top:1977px;width:334px;height:73px">Message</div>
    <a class="btn btn-green" style="left:726px;top:2057px;width:123px;height:36px;font-size:17px">Submit</a>
  </form>
</section>

<section class="about">
  <h2 class="abs section-title" style="left:0;top:2205px;font-size:29px;font-family:'Poppins',sans-serif">About Us</h2>
  <p class="abs about-text" style="top:2246px">Lorem ipsum dolor sit amet, consectetuer adipiscing elit, sed diam nonummy nibh euismod tincidunt ut laoreet dolore magna aliquam erat volutpat. Ut wisi enim ad minim veniam, quis nostrud exerci tation ullamcorper suscipit lobortis nisl ut aliquip ex ea commodo consequat. Duis autem vel eum iriure dolor in hendrerit in vulputate velit esse molestie consequat.</p>
  <p class="abs about-text" style="top:2323px">Lorem ipsum dolor sit amet, consectetuer adipiscing elit, sed diam nonummy nibh euismod tincidunt ut laoreet dolore magna aliquam erat volutpat. Ut wisi enim ad minim veniam, quis nostrud exerci tation ullamcorper suscipit lobortis nisl ut aliquip ex ea commodo consequat. Duis autem vel eum iriure dolor in hendrerit in vulputate velit esse molestie consequat.</p>
  <a class="btn btn-green" style="left:479px;top:2417px;width:239px;height:39px;font-size:18px;box-shadow:0 2px 3px rgba(0,0,0,.2)">Get Your Solution Now!</a>
</section>

<footer class="abs site-footer">Copyright © 2019 Brightfold Systems Inc. All Rights Reserved | Privacy</footer>

</body>
</html>
```